Workbook Cover Design

I am needing the cover for a workbook designed. I have attached a sample cover along with a few images giving an idea what at I am looking for. I'm open to new color schemes. I also attached a flyer of the event to give you an idea of the current color theme. The workbook will be approximately 8.5 x 11.

Title : Stewardship Workshop 202
Lorna Pell Ministries

On the cover I would like to have four sections with the following title under each section:
Evangelism (use photo similar to hands with cross)
Praying in Tongues (Photo similar to bird with heart or one with a mouth speaking)
Authority of the Believer (Photo with badge or similar)
Healing (Photo of man and wheelchair or similar)

Using silhouettes are okay, but I prefer not to have any actual faces of people.

```html
<!DOCTYPE html>
<html lang="en">
<head>
<meta charset="utf-8">
<title>Stewardship Workshop 202 — Workbook Cover</title>
<link rel="stylesheet" href="https://fonts.googleapis.com/css2?family=Lato:wght@300;400;700;900&family=Playball&display=block">
<style>
  :root {
    --stage: #4d4d4d;
    --paper: #ffffff;
    --navy: #000c2e;
    --navy-line: #0f1838;
    --purple-deep: #5a2266;
    --purple-bright: #9a2aaa;
    --ink: #111111;
    --label: #ffffff;
  }
  html, body {
    margin: 0;
    width: 1200px;
    height: 1200px;
    overflow: hidden;
    background: var(--stage);
  }
  .cover {
    position: absolute;
    left: 227px;
    top: 131px;
    width: 727px;
    height: 934px;
    display: block;
    box-shadow: 0 6px 18px rgba(0,0,0,0.35);
  }
  .section-title {
    font-family: "Lato", sans-serif;
    font-weight: 900;
    font-size: 34px;
    fill: var(--ink);
    text-anchor: middle;
  }
  .section-label {
    font-family: "Lato", sans-serif;
    font-weight: 900;
    font-size: 33px;
    fill: var(--label);
    text-anchor: middle;
  }
  .ministry-name {
    font-family: "Lato", sans-serif;
    font-weight: 400;
    font-size: 32px;
    fill: var(--label);
  }
  .workbook-title {
    font-family: "Playball", cursive;
    font-size: 84px;
    fill: var(--label);
    text-anchor: middle;
  }
  .workbook-title .course-number {
    font-family: "Lato", sans-serif;
    font-weight: 300;
    font-size: 76px;
  }
</style>
</head>
<body>
<svg class="cover" viewBox="0 0 1170 1503" xmlns="http://www.w3.org/2000/svg">
  <defs>
    <linearGradient id="purple-band" x1="0" y1="0" x2="0" y2="1">
      <stop offset="0" stop-color="var(--purple-deep)"/>
      <stop offset="0.2" stop-color="var(--purple-bright)"/>
      <stop offset="0.45" stop-color="var(--purple-bright)"/>
      <stop offset="0.55" stop-color="var(--purple-deep)"/>
      <stop offset="0.78" stop-color="var(--purple-bright)"/>
      <stop offset="1" stop-color="var(--purple-deep)"/>
    </linearGradient>

    <clipPath id="clip-healing"><polygon points="814,0 1170,0 1170,434 804,789 424,407"/></clipPath>
    <clipPath id="clip-tongues"><polygon points="402,426 782,812 404,1189 34,816"/></clipPath>
    <clipPath id="clip-evangelism"><polygon points="1170,485 1170,1212 440,1212 830,822"/></clipPath>

    <linearGradient id="sky-base" x1="0" y1="0" x2="0" y2="1">
      <stop offset="0" stop-color="#d8b8a2"/>
      <stop offset="0.35" stop-color="#9a6a52"/>
      <stop offset="0.6" stop-color="#b66a2e"/>
      <stop offset="1" stop-color="#f0b45a"/>
    </linearGradient>
    <radialGradient id="sky-sun" cx="0.5" cy="0.5" r="0.5">
      <stop offset="0" stop-color="#fff1c4"/>
      <stop offset="0.35" stop-color="#f6c46a" stop-opacity="0.85"/>
      <stop offset="1" stop-color="#e89a40" stop-opacity="0"/>
    </radialGradient>
    <radialGradient id="sky-cloud" cx="0.5" cy="0.5" r="0.5">
      <stop offset="0" stop-color="#2a140c" stop-opacity="0.75"/>
      <stop offset="1" stop-color="#2a140c" stop-opacity="0"/>
    </radialGradient>

    <radialGradient id="fire-base" cx="0.5" cy="0.5" r="0.6">
      <stop offset="0" stop-color="#5a1e0c"/>
      <stop offset="0.6" stop-color="#2a0c06"/>
      <stop offset="1" stop-color="#0c0403"/>
    </radialGradient>
    <radialGradient id="fire-flare" cx="0.5" cy="0.5" r="0.5">
      <stop offset="0" stop-color="#ffb347" stop-opacity="0.9"/>
      <stop offset="0.4" stop-color="#e0641c" stop-opacity="0.7"/>
      <stop offset="1" stop-color="#a0300c" stop-opacity="0"/>
    </radialGradient>
    <radialGradient id="soft-white" cx="0.5" cy="0.5" r="0.5">
      <stop offset="0" stop-color="#ffffff" stop-opacity="0.85"/>
      <stop offset="1" stop-color="#ffffff" stop-opacity="0"/>
    </radialGradient>

    <linearGradient id="light-base" x1="0" y1="0" x2="0" y2="1">
      <stop offset="0" stop-color="#a7a8ac"/>
      <stop offset="0.45" stop-color="#cdb49c"/>
      <stop offset="1" stop-color="#a07a5e"/>
    </linearGradient>
    <radialGradient id="light-burst" cx="0.5" cy="0.5" r="0.5">
      <stop offset="0" stop-color="#fffbe8"/>
      <stop offset="0.3" stop-color="#ffdca0" stop-opacity="0.9"/>
      <stop offset="1" stop-color="#e0a060" stop-opacity="0"/>
    </radialGradient>
    <linearGradient id="light-warm-edge" x1="0" y1="0" x2="1" y2="0">
      <stop offset="0" stop-color="#6a3e22" stop-opacity="0"/>
      <stop offset="1" stop-color="#6a3e22" stop-opacity="0.6"/>
    </linearGradient>

    <linearGradient id="badge-gold" x1="0" y1="0" x2="1" y2="1">
      <stop offset="0" stop-color="#f1d58a"/>
      <stop offset="0.5" stop-color="#c7973f"/>
      <stop offset="1" stop-color="#8a6420"/>
    </linearGradient>
  </defs>

  <rect class="page" x="0" y="0" width="1170" height="1503" fill="var(--paper)"/>

  <polygon class="purple-panel" points="0,403 378,403 0,782" fill="url(#purple-band)"/>
  <polygon class="purple-panel" points="0,830 380,1212 0,1212" fill="url(#purple-band)"/>

  <polyline class="header-rule" points="766,0 386,385 0,385" fill="none" stroke="var(--navy-line)" stroke-width="10"/>

  <g role="img" aria-label="Photo of a gold security officer badge">
    <path d="M246,42 L320,68 L330,110 L318,210 L246,278 L174,210 L162,110 L172,68 Z" fill="url(#badge-gold)"/>
  </g>
  <text class="section-title" x="238" y="319">AUTHORITY OF THE</text>
  <text class="section-title" x="238" y="359">BELIEVER</text>

  <g class="photo-healing" clip-path="url(#clip-healing)" role="img" aria-label="Photo of a silhouetted man raising his fist against a sunset sky">
    <rect x="400" y="0" width="770" height="800" fill="url(#sky-base)"/>
    <ellipse cx="600" cy="400" rx="320" ry="170" fill="url(#sky-cloud)"/>
    <ellipse cx="1080" cy="330" rx="220" ry="120" fill="url(#sky-cloud)" opacity="0.6"/>
    <ellipse cx="960" cy="720" rx="380" ry="300" fill="url(#sky-sun)"/>
  </g>
  <text class="section-label" x="666" y="472">HEALING</text>

  <g class="photo-evangelism" clip-path="url(#clip-evangelism)" role="img" aria-label="Photo of open raised hands before a glowing cross">
    <rect x="430" y="480" width="740" height="740" fill="url(#light-base)"/>
    <rect x="900" y="480" width="270" height="740" fill="url(#light-warm-edge)"/>
    <ellipse cx="1010" cy="1000" rx="420" ry="360" fill="url(#light-burst)"/>
  </g>
  <text class="section-label" x="850" y="1158">EVANGELISM</text>

  <g class="photo-tongues" clip-path="url(#clip-tongues)" role="img" aria-label="Illustration of a white dove flying over a flaming heart">
    <rect x="30" y="420" width="760" height="780" fill="url(#fire-base)"/>
    <ellipse cx="330" cy="720" rx="240" ry="220" fill="url(#fire-flare)"/>
    <ellipse cx="520" cy="700" rx="220" ry="200" fill="url(#fire-flare)" opacity="0.85"/>
    <ellipse cx="400" cy="960" rx="200" ry="180" fill="url(#fire-flare)" opacity="0.7"/>
    <ellipse cx="520" cy="880" rx="220" ry="110" fill="url(#soft-white)" opacity="0.55"/>
  </g>
  <text class="section-label" x="415" y="790">PRAYING IN TONGUES</text>

  <rect class="footer-band" x="0" y="1222" width="1170" height="281" fill="var(--navy)"/>
  <text class="ministry-name" x="217" y="1286">Lorna Pell Ministries</text>
  <text class="workbook-title" x="560" y="1408">Stewardship Workshop <tspan class="course-number">202</tspan></text>
</svg>
</body>
</html>
```